Flyer needed for Seminar

Hello,
We are looking for eye-catching, inspiring marketing material for an educational seminar. We need 4 x 6 clubcards with the following info:

CLUBCARD FRONT:

Verander Academy Presents:

Stillness: Under The Surface
Unlock the hidden treasures of prayer
By. Shaykh Idris Kamal Al-Furati

Dates:Jan 23-25, 2015
Timings: Fri - 7pm - 9:30 pm; Sat/Sun - 9am - 8 pm

Location: Riverbend Grand Suites at Oakhaven Square
4385 Millbrook Lane, Plano, TX 75093

Seating is Limited. Register Today!
www.VeranderAcademy,com

CLUBCARD BACK:
In this unique seminar, learn how to connect spiritually with your Creator through prayer. Let us teach you the hidden meanings behind salah and why it is essential to your existence. Not only will the instructor impart the skills you'll need to master khushoo but he will delve more deeply, into the inner realms and intricacies of this ibadaa. As a result, the prayer will no longer be regarded as a mechanical chore, but an intimate meeting with the Divine. Through such insight, we hope you will leave this non-fiqh seminar with an awakened and unparalleled understanding of this fundamental pillar of Islam.

www.VeranderAcademy.com
For more info: Email - info@veranderacademy.com; Phone - 1-877-Verand4

Reason: I really appreciate all the submissions but am looking for something more eye-catching, something that really stirs ones interest and relates to the title of the seminar. Thank you!

```html
<!DOCTYPE html>
<html lang="en">
<head>
<meta charset="utf-8">
<title>Under The Surface – Seminar Club Card</title>
<link rel="stylesheet" href="https://fonts.googleapis.com/css2?family=Cinzel:wght@400;500&family=Libre+Baskerville:wght@400;700&family=Questrial&display=swap">
<style>
  :root {
    --backdrop: #e8e5de;
    --paper: #ffffff;
    --gold-edge: #d9b02a;
    --gold-light: #f1dc8a;
    --gold-mid: #d8ae3a;
    --gold-deep: #b8891f;
    --ink-gold: #a8872e;
    --ink-title: #8f7338;
    --ink-grey: #8a8478;
    --ink-dark: #5c5446;
  }
  * { margin: 0; padding: 0; box-sizing: border-box; }
  html, body { width: 1200px; height: 900px; overflow: hidden; }
  body { background: var(--backdrop); position: relative; }

  .club-card {
    position: absolute;
    left: 310px; top: 15px;
    width: 580px; height: 870px;
    background: var(--paper);
    border: 7px solid var(--gold-edge);
    box-shadow: 0 6px 24px rgba(0,0,0,0.12);
  }
  .card-art { position: absolute; inset: 0; width: 566px; height: 856px; }

  .card-copy {
    position: absolute;
    left: 0; right: 0; top: 0;
    text-align: center;
  }
  .presenter {
    position: absolute; top: 178px; left: 0; right: 0;
    font: 700 13px "Libre Baskerville", serif;
    color: var(--ink-gold);
  }
  .title {
    position: absolute; top: 205px; left: 0; right: 0;
    font-family: "Cinzel", serif;
    font-weight: 400;
    color: var(--ink-title);
    line-height: 1;
  }
  .title-line { display: block; font-size: 52px; letter-spacing: 1px; }
  .title-join {
    display: flex; align-items: center; justify-content: center; gap: 10px;
    font-size: 20px; letter-spacing: 2px; margin: 2px 0 4px;
  }
  .title-join::before, .title-join::after {
    content: ""; width: 62px; height: 1px; background: var(--gold-mid);
  }
  .tagline {
    position: absolute; top: 344px; left: 0; right: 0;
    font: 700 12.5px "Libre Baskerville", serif;
    color: var(--ink-gold);
  }
  .divider {
    position: absolute; top: 372px; left: 50%; width: 46px; margin-left: -23px;
    height: 2px; background: var(--gold-deep);
  }
  .speaker {
    position: absolute; top: 388px; left: 0; right: 0;
    font: 700 12.5px/1.5 "Libre Baskerville", serif;
    color: var(--ink-gold);
  }
  .schedule {
    position: absolute; top: 448px; left: 0; right: 0;
    font: 13px/1.45 "Questrial", sans-serif;
    color: var(--ink-grey);
  }
  .schedule-dot {
    display: block; width: 5px; height: 5px; border-radius: 50%;
    background: var(--gold-mid); margin: 4px auto 0;
  }
  .venue {
    position: absolute; top: 520px; left: 0; right: 0;
    font: 13px/1.45 "Libre Baskerville", serif;
    color: var(--ink-dark);
  }
  .call-to-action {
    position: absolute; left: 0; right: 0; bottom: 14px;
    font: 14px "Questrial", sans-serif;
    color: var(--ink-grey);
    text-align: center;
    letter-spacing: 0.3px;
  }
  .call-to-action .site { color: var(--ink-gold); }
</style>
</head>
<body>
  <article class="club-card">
    <svg class="card-art" viewBox="0 0 566 856" aria-hidden="false">
      <defs>
        <linearGradient id="ornament-gold" x1="0" y1="0" x2="1" y2="1">
          <stop offset="0" stop-color="#f4e3a0"/>
          <stop offset="0.5" stop-color="#e2bf57"/>
          <stop offset="1" stop-color="#f0d98a"/>
        </linearGradient>
      </defs>
      <rect class="ornament-field" x="14" y="14" width="538" height="782" fill="url(#ornament-gold)"
            role="img" aria-label="Gold floral arabesque border of scrolling vines, leaves and blossoms"/>
      <path class="cartouche-glow" fill="none" stroke="var(--gold-light)" stroke-width="9"
            d="M283 100 C313 140,393 160,433 200 C463 240,453 320,423 370 C398 410,388 435,403 470 C433 520,443 590,413 650 C383 700,313 720,283 760 C253 720,183 700,153 650 C123 590,133 520,163 470 C178 435,168 410,143 370 C113 320,103 240,133 200 C173 160,253 140,283 100 Z"/>
      <path class="cartouche" fill="var(--paper)" stroke="var(--gold-mid)" stroke-width="1.5"
            d="M283 100 C313 140,393 160,433 200 C463 240,453 320,423 370 C398 410,388 435,403 470 C433 520,443 590,413 650 C383 700,313 720,283 760 C253 720,183 700,153 650 C123 590,133 520,163 470 C178 435,168 410,143 370 C113 320,103 240,133 200 C173 160,253 140,283 100 Z"/>
      <rect class="footer-band" x="0" y="796" width="566" height="60" fill="var(--paper)"/>
    </svg>

    <div class="card-copy">
      <p class="presenter">Verander Academy Presents</p>
      <h1 class="title">
        <span class="title-line">Under</span>
        <span class="title-join">THE</span>
        <span class="title-line">Surface</span>
      </h1>
      <p class="tagline">Unlock the hidden treasures of prayer</p>
      <span class="divider"></span>
      <p class="speaker">By<br>Shaykh Idris Kamal Al-Furati</p>
      <p class="schedule">
        Jan 23-25, 2015<br>
        Fri - 7PM - 9:30 PM<br>
        Sat/Sun - 9AM - 8 PM
        <span class="schedule-dot"></span>
      </p>
      <p class="venue">
        Plano<br>
        Riverbend Grand Suites<br>
        at Oakhaven Square<br>
        4385 Millbrook Lane,<br>
        Plano, TX 75093
      </p>
    </div>

    <p class="call-to-action">Seating is Limited. Register Today! &nbsp;|&nbsp; <span class="site">www.VeranderAcademy.com</span></p>
  </article>
</body>
</html>
```